Beautiful, sharp, website design for family-run property development company.

We are property developers in Kent (south east of London) who want to see the local town change. We are the only local property developer that is a family run business, focussing primarily on converting old, dilapidated Victorian buildings into beautiful residential spaces. Unlike other national developers, we work to regenerate buildings to create new employment opportunities, housing, and revive the town Centre .

Target Market(s)

1. Investors and Joint Venture partners - people with money to invest in property
2. Buyers of property - 25 to 40 year old, young professionals.
3. Commercial funders (people lending money to our projects
4. Professional team: Architects, builders, Estate agent who want to work with us

Industry/Entity Type

Real Estate Development

Coding

Number of Pages Required

Font styles to use
Other font styles liked:
• Please follow the brief of stylish, elegant, modern

Colors

Designer to choose colors to be used in the design.

Requirements
Must have
• Please use these websites as a reference of what we are looking to achieve.
• http://brellmoorhomes.com/#page5
• https://fernwick.co.uk/
• http://ambertide.co.uk/
• http://www.theharroweyestates.co.uk/about-harrowey
• Clean, simple, elegant, minimal design.
• Images of interiors of houses that have been converted from old buildings
• Images of farm buildings e.g. barns that have been converted to new homes or offices. Images of properties that may have been an old factory or old commercial property that is now a trendy apartment.
• Please use images of properties and interiors that are from the South East of England (including Kent, Surrey, Sussex, Hampshire, Dorset). There is a distinct style of housing in this part of England.
Nice to have
• Colours consistent with our brand colour palette (attached)

```html
<!DOCTYPE html>
<html lang="en">
<head>
<meta charset="utf-8">
<title>Larchwell Property</title>
<link href="https://fonts.googleapis.com/css2?family=Montserrat:wght@300;400;500;600&family=Libre+Baskerville&display=swap" rel="stylesheet">
<style>
:root{
  --ink:#2b2b2b;
  --muted:#6b6b6b;
  --sage:#6f8f86;
  --mint:#f0f4ec;
  --panel:#c6ceca;
  --white:#ffffff;
  --line:#b9bfbb;
  --shade:rgba(40,40,40,.72);
}
*{margin:0;padding:0;box-sizing:border-box}
html,body{width:1200px;height:3241px;overflow:hidden}
body{position:relative;background:var(--white);font-family:'Montserrat',sans-serif;color:var(--ink)}
.abs{position:absolute}
.site-header{left:0;top:0;width:1200px;height:91px}
.brand{left:27px;top:28px;display:flex;align-items:center;gap:10px}
.brand-mark{width:30px;height:30px;border:2px solid var(--sage);border-radius:50%}
.brand-name{font-size:17px;font-weight:400;color:var(--sage);letter-spacing:.5px;line-height:1.1}
.brand-name small{display:block;font-size:7px;letter-spacing:3px;text-align:center}
.main-nav{right:56px;top:38px;display:flex;gap:29px;font-size:11px;letter-spacing:3.4px;font-weight:500}
.main-nav a{color:var(--ink);text-decoration:none}
.main-nav a.active{color:var(--sage);border-bottom:1px solid var(--sage);padding-bottom:4px}
.photo{display:block}
.hero-photo{left:436px;top:91px;width:764px;height:587px;background:linear-gradient(100deg,#dcdcdc 0%,#c9c7c4 35%,#9a6e52 60%,#7b5038 100%)}
.rule{display:block;width:34px;height:1px;background:var(--ink)}
.hero-copy{left:58px;top:193px;width:345px}
.hero-copy h1{font-weight:400;font-size:34px;line-height:56px;letter-spacing:1.5px;margin-top:10px}
.hero-copy p{font-size:14px;line-height:26px;color:var(--muted);margin-top:26px;letter-spacing:.4px}
.hero-arrow{left:58px;top:476px}
.about-band{left:0;top:636px;width:665px;height:435px;background:var(--mint)}
.about-copy{left:58px;top:755px;width:550px}
.about-copy h2{font-weight:400;font-size:34px;letter-spacing:2px;margin-top:10px}
.about-copy p{font-size:13.5px;line-height:25.7px;color:var(--muted);margin-top:28px}
.about-copy a{color:var(--ink)}
.stats{left:737px;top:770px;width:305px;font-size:13.5px}
.stats .row{display:flex;justify-content:space-between;height:56px;padding-top:6px;border-bottom:1px solid var(--line);margin-bottom:0}
.stats .row:not(:first-child){padding-top:18px}
.stats .label{color:var(--sage)}
.reno-photo{left:0;top:1071px;width:1200px;height:366px;background:linear-gradient(90deg,#a8663c 0%,#c48a5a 25%,#8f99a6 45%,#d9d8d4 60%,#e7c6b4 100%)}
.reno-box{left:314px;top:1182px;width:571px;height:204px;background:var(--shade);text-align:center;color:var(--white)}
.reno-box h3{font-family:'Libre Baskerville',serif;font-weight:400;font-size:25px;letter-spacing:2.5px;margin-top:64px}
.reno-box .rule{background:var(--white);margin:14px auto 0}
.reno-box p{font-size:14px;letter-spacing:.8px;margin-top:22px}
.featured{left:0;top:1437px;width:1200px;height:763px;background:var(--mint)}
.featured-title{left:0;top:1503px;width:1200px;text-align:center}
.featured-title .rule{margin:0 auto}
.featured-title h2{font-weight:400;font-size:34px;letter-spacing:2px;margin-top:10px}
.card{width:336px;height:231px;color:var(--white);text-align:center}
.card .accent{position:absolute;left:10px;width:2px;background:var(--white)}
.card h4{font-weight:500;font-size:24px;letter-spacing:.5px}
.card p{font-size:16px;letter-spacing:1.2px;margin-top:4px;font-weight:300}
.card .stack{position:absolute;left:0;width:100%}
.c1{background:linear-gradient(160deg,#5c5a52,#3f3c36)}
.c2{background:linear-gradient(170deg,#4d5a45,#6d7a5c 60%,#7a6a6a)}
.c3{background:linear-gradient(170deg,#5a6a66,#76867c 55%,#4d6a3e)}
.c4{background:linear-gradient(160deg,#8c8a7c,#6e6a5c 60%,#8a7a66)}
.c5{background:linear-gradient(170deg,#3b3b38,#5a5046 60%,#4a4a46)}
.c6{background:linear-gradient(160deg,#6a3c34,#7a6e66 55%,#9aa4a6)}
.card .veil{position:absolute;inset:0;background:rgba(30,30,30,.35)}
.down-arrow{left:1135px;top:2055px}
.split-left{left:0;top:2200px;width:601px;height:260px;background:linear-gradient(90deg,#e8eae8,#f4f4f2 50%,#a9b6b4)}
.split-right{left:601px;top:2200px;width:599px;height:260px;background:linear-gradient(180deg,#a9c6e4 0%,#dfe6ea 45%,#6c8f4e 75%,#5a8a3a 100%)}
.panel{left:0;top:2460px;width:1200px;height:296px;background:var(--panel)}
.divider{left:601px;top:2490px;width:1px;height:230px;background:var(--ink)}
.offer{width:460px;text-align:center}
.offer h3{font-weight:400;font-size:23px;line-height:30px}
.offer p{font-size:11.5px;line-height:20px;margin-top:22px}
.btn{display:inline-block;width:190px;height:36px;line-height:34px;border:2px solid var(--ink);font-size:11.5px;letter-spacing:2px;margin-top:40px;color:var(--ink);text-decoration:none}
.arrow-left{left:26px;top:2728px}
.arrow-right{left:1150px;top:2728px}
.footer-photo{left:0;top:2756px;width:1200px;height:485px;background:linear-gradient(90deg,#2a2826,#45413c 40%,#3c3a36 70%,#55514a)}
.footer-veil{left:0;top:2756px;width:1200px;height:485px;background:rgba(20,20,20,.35)}
.footer-brand{left:0;top:2975px;width:1200px;text-align:center;color:var(--white)}
.footer-brand .name{font-size:44px;font-weight:500;letter-spacing:1px;line-height:1}
.footer-brand .sub{font-size:19px;letter-spacing:7px;margin-top:10px;font-weight:400}
.footer-nav{left:0;top:3081px;width:1200px;display:flex;justify-content:center;font-size:11px;letter-spacing:3.6px;font-weight:600}
.footer-nav a{color:var(--white);text-decoration:none;padding:0 22px;border-left:2px solid var(--white);line-height:18px}
.footer-nav a:first-child{border-left:none}
.copyright{left:0;top:3131px;width:1200px;text-align:center;color:var(--white);font-size:12px;font-weight:500}
.social{left:0;top:3170px;width:1200px;display:flex;justify-content:center;gap:22px}
.social span{width:31px;height:31px;border:2px solid var(--white);border-radius:50%}
</style>
</head>
<body>

<header class="site-header abs">
  <div class="brand abs"><span class="brand-mark"></span><span class="brand-name">LARCHWELL<small>PROPERTY</small></span></div>
  <nav class="main-nav abs">
    <a class="active" href="#">HOME</a><a href="#">PROJECTS</a><a href="#">ABOUT</a><a href="#">CONTACT</a>
  </nav>
</header>

<div class="hero-photo photo abs" role="img" aria-label="Modern dining room with white table, sofas, pendant lamps and a timber-clad wall"></div>
<section class="hero-copy abs">
  <span class="rule"></span>
  <h1>There is Beauty In Simplicity.</h1>
  <p>The point of using Lorem Ipsum is that it has a more-or-less normal distribution of letters, as opposed to using 'Content here, content here'.</p>
</section>
<svg class="hero-arrow abs" width="16" height="24" viewBox="0 0 16 24" fill="none" stroke="#555" stroke-width="1.3"><path d="M8 1v21M2 16l6 6 6-6"/></svg>

<div class="about-band abs"></div>
<section class="about-copy abs">
  <span class="rule"></span>
  <h2>What We Do</h2>
  <p>Lorem ipsum dolor sit amet, consectetur adipiscing elit, sed do eiusmod tempor incididunt ut labore et dolore magna aliqua. Quis ipsum suspendisse ultrices gravida. Risus commodo viverra maecenas accumsan lacus vel facilisis. Lorem ipsum dolor sit amet, consectetur adipiscing elit, sed do eiusmod tempor incididunt ut labore <a href="#">get in touch</a>
  <svg width="22" height="10" viewBox="0 0 22 10" fill="none" stroke="#555" stroke-width="1.2" style="margin-left:14px"><path d="M0 5h20M16 1l4 4-4 4"/></svg></p>
</section>
<dl class="stats abs">
  <div class="row"><dt class="label">Founded</dt><dd>2009</dd></div>
  <div class="row"><dt class="label">Projects Completed</dt><dd>135+</dd></div>
  <div class="row"><dt class="label">Team</dt><dd>9</dd></div>
</dl>

<div class="reno-photo photo abs" role="img" aria-label="Split view of a finished living room and a room under renovation"></div>
<section class="reno-box abs">
  <h3>RENOVATION IN PROCESS</h3>
  <span class="rule"></span>
  <p>Lorem ipsum dolor sit amet, consectetur adipiscing</p>
</section>

<div class="featured abs"></div>
<div class="featured-title abs"><span class="rule"></span><h2>Featured Pojects</h2></div>

<article class="card c1 abs" style="left:86px;top:1607px" role="img" aria-label="Old weathered timber house">
  <div class="veil"></div>
  <span class="accent" style="top:66px;height:80px"></span>
  <div class="stack" style="top:40px"><h4>Lorem ipsum dolor</h4>
  <p style="font-size:13px;line-height:17px;letter-spacing:.3px;margin:20px 34px 0">Amet, consecteturingsed do eiusmod tempor incididunt ut labore et dolore magna aliqua. Quis ipsum suspendisse ultrices gravida. Risus commodo viverra maecenas facilisis.</p></div>
</article>
<article class="card c2 abs" style="left:431px;top:1607px" role="img" aria-label="Stone house surrounded by garden">
  <div class="veil"></div><span class="accent" style="top:168px;height:62px"></span>
  <div class="stack" style="top:146px"><h4>Lorem ipsum dolor</h4><p>Amet, consecteturing</p></div>
</article>
<article class="card c3 abs" style="left:776px;top:1607px" role="img" aria-label="Colonial house with veranda and trees">
  <div class="veil"></div><span class="accent" style="top:168px;height:62px"></span>
  <div class="stack" style="top:146px"><h4>Lorem ipsum dolor</h4><p>Amet, consecteturing</p></div>
</article>
<article class="card c4 abs" style="left:86px;top:1846px" role="img" aria-label="Derelict interior with graffiti walls">
  <div class="veil"></div><span class="accent" style="top:136px;height:94px"></span>
  <div class="stack" style="top:146px"><h4>Lorem ipsum dolor</h4><p>Amet, consecteturing</p></div>
</article>
<article class="card c5 abs" style="left:431px;top:1846px" role="img" aria-label="Abandoned brick building facade">
  <div class="veil"></div><span class="accent" style="top:136px;height:94px"></span>
  <div class="stack" style="top:146px"><h4>Lorem ipsum dolor</h4><p>Amet, consecteturing</p></div>
</article>
<article class="card c6 abs" style="left:776px;top:1846px" role="img" aria-label="Brick house with blue door and white picket fence">
  <div class="veil"></div><span class="accent" style="top:136px;height:94px"></span>
  <div class="stack" style="top:146px"><h4>Lorem ipsum dolor</h4><p>Amet, consecteturing</p></div>
</article>
<svg class="down-arrow abs" width="16" height="24" viewBox="0 0 16 24" fill="none" stroke="#444" stroke-width="1.4"><path d="M8 1v21M2 16l6 6 6-6"/></svg>

<div class="split-left photo abs" role="img" aria-label="Bright empty commercial space with large windows"></div>
<div class="split-right photo abs" role="img" aria-label="Modern residential villa with pool, lawn and palm trees"></div>
<div class="panel abs"></div>
<div class="divider abs"></div>
<section class="offer abs" style="left:80px;top:2491px">
  <h3>Renovating and Regenerating&nbsp; old&nbsp; to new Commercial</h3>
  <p>Lorem ipsum dolor sit amet, consectetur adipiscing elit,<br>sed do eiusmod tempor incididunt ut labore et dolore<br>magna aliqua. Quis ipsum suspendisse ultrices gravida.</p>
  <a class="btn" href="#">VIEW MORE</a>
</section>
<section class="offer abs" style="left:671px;top:2493px">
  <h3>Renovating and Regenerating&nbsp; old&nbsp; to new Residencial</h3>
  <p>Lorem ipsum dolor sit amet, consectetur adipiscing elit,<br>sed do eiusmod tempor incididunt ut labore et dolore<br>magna aliqua. Quis ipsum suspendisse ultrices gravida.</p>
  <a class="btn" href="#" style="margin-top:46px">VIEW MORE</a>
</section>
<svg class="arrow-left abs" width="24" height="16" viewBox="0 0 24 16" fill="none" stroke="#333" stroke-width="1.4"><path d="M23 8H2M8 2L2 8l6 6"/></svg>
<svg class="arrow-right abs" width="24" height="16" viewBox="0 0 24 16" fill="none" stroke="#333" stroke-width="1.4"><path d="M1 8h21M16 2l6 6-6 6"/></svg>

<footer>
  <div class="footer-photo photo abs" role="img" aria-label="Dim interior with sculptures, stacked firewood and tall windows"></div>
  <div class="footer-veil abs"></div>
  <div class="footer-brand abs"><div class="name">LARCHWELL</div><div class="sub">PROPERTY</div></div>
  <nav class="footer-nav abs"><a href="#">HOME</a><a href="#">PROJECTS</a><a href="#">ABOUT</a><a href="#">CONTACT</a></nav>
  <p class="copyright abs">Copyrights ©. 2020 Allrights Reserved.</p>
  <div class="social abs"><span aria-label="Social link"></span><span aria-label="Social link"></span><span aria-label="Social link"></span></div>
</footer>

</body>
</html>
```